Morden, Creative, Unique, Independent Wine Shop

1. We are a brand new wine shop located in Melbourne Australia, we have our logo already, simply use the logo to design a business card.
2. I have uploaded our logo in two versions, with or without shadow, any of them is acceptable.
3. Make it as creative and unique as possible, no limitation of shape, color combination, geometry pattern, fonts, composing etc.
3. Info on the card:
- Brambleford Wine Cellar (Not very necessary if logo is obviously shown)
- 42 Ferncastle Steet, Larkmoor, Tasmania, Australia 7254
- +61 3 9018 4637
- www.bramblefordwinecellar.com.au
- bramblefordwinecellar@mailvista.com
- Additional icons: Google, Instagram, Facebook, Twitter
4. Once again, forget it is a commercial card, make it special.

```html
<!DOCTYPE html>
<html lang="en">
<head>
<meta charset="utf-8">
<title>Brambleford Wine Cellar — Business Card</title>
<link rel="stylesheet" href="https://fonts.googleapis.com/css2?family=Cinzel:wght@400&family=Montserrat:wght@400;500&display=swap">
<style>
  :root {
    --backdrop: #f5f5f5;
    --card: #ffffff;
    --wine: #8b1a2b;
    --ink: #3a3a3a;
    --icon: #2e2e2e;
    --wave-deep: #d42b4a;
    --wave-mid: #de5a72;
    --wave-soft: #eb8fa0;
  }
  * { box-sizing: border-box; margin: 0; padding: 0; }
  html, body {
    width: 1200px;
    height: 1200px;
    overflow: hidden;
    background: var(--backdrop);
  }
  .card-pair {
    position: absolute;
    left: 251px;
    top: 337px;
    display: flex;
    gap: 41px;
  }
  .card {
    position: relative;
    width: 340px;
    height: 602px;
    background: var(--card);
    border-radius: 17px;
    overflow: hidden;
  }
  .card__waves {
    position: absolute;
    left: 0;
    top: 0;
    width: 100%;
    height: 100%;
  }

  .wordmark {
    position: absolute;
    left: 0;
    right: 0;
    text-align: center;
    line-height: 1;
  }
  .wordmark__name {
    display: block;
    font-family: "Cinzel", serif;
    font-weight: 400;
    font-size: 38px;
    color: var(--wine);
  }
  .wordmark__sub {
    display: block;
    font-family: "Montserrat", sans-serif;
    font-weight: 500;
    font-size: 16px;
    letter-spacing: 3px;
    text-transform: uppercase;
    color: var(--ink);
    margin-top: 6px;
  }
  .card--front .wordmark { top: 118px; }

  .contact {
    position: absolute;
    left: 0;
    right: 0;
    top: 0;
    list-style: none;
    font-family: "Montserrat", sans-serif;
    font-size: 10.5px;
    letter-spacing: 0.5px;
    color: var(--ink);
  }
  .contact__row {
    position: absolute;
    left: 35px;
    right: 4px;
    display: flex;
    align-items: flex-start;
  }
  .contact__icon {
    width: 22px;
    height: 22px;
    flex: none;
    stroke: var(--icon);
    fill: none;
    stroke-width: 1.5;
    stroke-linecap: round;
    stroke-linejoin: round;
  }
  .contact__text {
    margin-left: 50px;
    line-height: 1.45;
    padding-top: 3px;
    white-space: nowrap;
  }
  .contact__row--address { top: 216px; }
  .contact__row--address .contact__icon { margin-top: 8px; }
  .contact__row--mail { top: 284px; }
  .contact__row--phone { top: 319px; }
  .contact__row--web { top: 356px; }

  .social {
    position: absolute;
    top: 421px;
    left: 101px;
    display: flex;
    gap: 9px;
    list-style: none;
  }
  .social__dot {
    width: 27px;
    height: 27px;
    border: 1.8px solid var(--icon);
    border-radius: 50%;
  }

  .card--back .wordmark { top: 198px; }
  .card--back .wordmark__name { color: var(--wine); }
  .card--back .wordmark__sub {
    font-family: "Cinzel", serif;
    font-weight: 400;
    color: var(--wine);
    font-size: 18px;
  }
  .card--back .brand-dot {
    position: absolute;
    left: 150px;
    top: 140px;
    width: 40px;
    height: 40px;
    border-radius: 50%;
    background: var(--wine);
  }
</style>
</head>
<body>
  <main class="card-pair">
    <section class="card card--front" aria-label="Card front with contact details">
      <svg class="card__waves" viewBox="0 0 340 602" preserveAspectRatio="none" aria-hidden="true">
        <path d="M0,528 C70,516 170,494 260,482 L340,470 L340,602 L0,602 Z" fill="var(--wave-soft)"/>
        <path d="M340,408 C300,440 270,500 200,520 C120,540 50,548 0,590 L0,602 L340,602 Z" fill="var(--wave-deep)"/>
        <path d="M0,560 C60,540 130,530 200,520 C120,548 60,566 0,596 Z" fill="var(--wave-mid)" opacity="0.7"/>
      </svg>

      <h1 class="wordmark">
        <span class="wordmark__name">Brambleford</span>
        <span class="wordmark__sub">Wine Cellar</span>
      </h1>

      <ul class="contact">
        <li class="contact__row contact__row--address">
          <svg class="contact__icon" viewBox="0 0 24 24" aria-hidden="true"><path d="M3 11 L12 3 L21 11"/><path d="M5 9.5 V20 H19 V9.5"/><path d="M10 20 V14 H14 V20"/></svg>
          <span class="contact__text">42 Ferncastle Steet,<br>Larkmoor, Tasmania,<br>Australia 7254</span>
        </li>
        <li class="contact__row contact__row--mail">
          <svg class="contact__icon" viewBox="0 0 24 24" aria-hidden="true"><rect x="2.5" y="5" width="19" height="14"/><path d="M2.5 5 L12 13 L21.5 5"/></svg>
          <span class="contact__text">bramblefordwinecellar@mailvista.com</span>
        </li>
        <li class="contact__row contact__row--phone">
          <svg class="contact__icon" viewBox="0 0 24 24" aria-hidden="true"><path d="M5 3 H9 L11 8 L8.5 9.5 C9.5 12 12 14.5 14.5 15.5 L16 13 L21 15 V19 C21 20 20 21 19 21 C10 20.5 3.5 14 3 5 C3 4 4 3 5 3 Z"/></svg>
          <span class="contact__text">+61 3 9018 4637</span>
        </li>
        <li class="contact__row contact__row--web">
          <svg class="contact__icon" viewBox="0 0 24 24" aria-hidden="true"><circle cx="12" cy="12" r="9.5"/><ellipse cx="12" cy="12" rx="4" ry="9.5"/><path d="M2.5 12 H21.5"/></svg>
          <span class="contact__text">www.bramblefordwinecellar.com.au</span>
        </li>
      </ul>

      <ul class="social" aria-label="Social profiles">
        <li class="social__dot"></li>
        <li class="social__dot"></li>
        <li class="social__dot"></li>
        <li class="social__dot"></li>
      </ul>
    </section>

    <section class="card card--back" aria-label="Card back with brand name">
      <svg class="card__waves" viewBox="0 0 340 602" preserveAspectRatio="none" aria-hidden="true">
        <path d="M0,290 C50,288 86,360 108,432 C140,520 240,566 340,590 L340,602 L0,602 Z" fill="var(--wave-soft)"/>
        <path d="M0,400 C90,420 170,480 250,560 L0,602 Z" fill="var(--wave-mid)" opacity="0.75"/>
        <path d="M0,565 C100,570 220,560 340,582 L340,602 L0,602 Z" fill="var(--wave-deep)"/>
      </svg>
      <span class="brand-dot" aria-hidden="true"></span>
      <p class="wordmark">
        <span class="wordmark__name">Brambleford</span>
        <span class="wordmark__sub">Wine Cellar</span>
      </p>
    </section>
  </main>
</body>
</html>
```